TELVANO End User Instruction Guide

I need to create a 5 to 7-page instruction guides for customers who purchased a phone system from our company. The document is a quick reference guide that will help end-users learn how to set up and use their new desk phone and software applications. I need the guide to be 3 x 5 or 6 x 8 in size and will fold like a book.

Target Market(s)

Business users / Corvana Desk Phone Users / TelVANO Portal users

Industry/Entity Type

Telecommunications

Font styles to use
Serif

Colors
0758a5
ffffff

Requirements
Must have
• Need to have step-by-step instructions that include the information from the QuickStart guide I provided. I need to see an image of the phone with an arrow pointing to the key on the phone that should be pressed. For example, when checking voicemail the Messages key is pressed and I want to highlight this button or call it out somehow.

I need to have three pages for setup instructions, one page for shortcuts or features codes and our support contacts on the last page.
Nice to have
• I want to have a page for notes that the end-user can use during training. I would also like to have a blank space next to passwords and user ID's so they can be filled out with specific details that are provided during their training. For example, in the voicemail section, I include a default PIN. I would like to leave this blank and let the end-user fill it out during training.
Should not have
• Complex shapes and designs. I like straight lines and a simple easy to understand layout.

```html
<!DOCTYPE html>
<html lang="en">
<head>
<meta charset="utf-8">
<title>TELVANO Quick Reference – Feature Codes & Support</title>
<link href="https://fonts.googleapis.com/css2?family=Roboto:wght@300;400;500;700&display=swap" rel="stylesheet">
<style>
  :root{
    --brand-blue:#0758a5;
    --brand-dark:#2f3a44;
    --ink:#1a1a1a;
    --paper:#ffffff;
  }
  *{margin:0;padding:0;box-sizing:border-box}
  html,body{width:1200px;height:800px;overflow:hidden;background:var(--paper)}
  body{position:relative;font-family:"Roboto",sans-serif;color:var(--ink)}
  .wordmark{position:absolute;display:flex;align-items:center;gap:6px;color:var(--brand-dark);font-family:"Roboto",sans-serif;font-weight:700;letter-spacing:.5px}
  .wordmark .mark{background:var(--brand-blue);display:block}
  .wordmark--small{left:31px;top:32px;font-size:16px}
  .wordmark--small .mark{width:12px;height:12px}
  .wordmark--large{left:780px;top:340px;font-size:38px}
  .wordmark--large .mark{width:30px;height:30px}

  .page-spine{position:absolute;left:31px;top:75px;width:3px;height:725px;background:var(--brand-blue)}
  .page-foot{position:absolute;left:0;top:769px;width:598px;height:3px;background:var(--brand-blue)}
  .page-number{position:absolute;left:28px;top:762px;font-size:10px;background:var(--paper);padding:0 1px;line-height:14px}

  .codes{position:absolute;left:58px;top:73px;width:512px;border-collapse:collapse;font-size:10.6px;font-weight:300;line-height:13px}
  .codes td,.codes th{border:1px solid var(--brand-blue);padding:0 3px;vertical-align:middle;text-align:left}
  .codes col.code{width:94px}
  .codes th{background:var(--brand-blue);color:var(--paper);font-weight:400;text-align:center}
  .codes .link{color:var(--brand-blue)}

  .contact{position:absolute;left:600px;width:600px;display:flex;align-items:center;justify-content:space-between}
  .contact .rule{width:166px;height:3px;background:var(--brand-blue)}
  .contact .value{font-size:14px;font-weight:500;color:var(--brand-blue);text-align:center;flex:1}
  .contact--email{top:526px}
  .contact--phone{top:564px}
  .contact--web{top:600px}
</style>
</head>
<body>
  <div class="wordmark wordmark--small"><span class="mark"></span>TELVANO</div>
  <div class="page-spine"></div>

  <table class="codes">
    <colgroup><col class="code"><col></colgroup>
    <tr><th>Star Code</th><th>Feature Description</th></tr>
    <tr><td>*46</td><td>Hotdesking (Log Out) - Requires Password of current logged in user.</td></tr>
    <tr><td>*48</td><td>Ask caller to enter PIN before connecting call</td></tr>
    <tr><td>*49</td><td>Ask caller to enter extension # before connecting call</td></tr>
    <tr><td>*50{ext}</td><td>Auto Answer/Intercom (3 or 4 Digit Ext) This feature does not work with SLA.</td></tr>
    <tr><td>*55{Parking Lot}</td><td>Retrieve a call from a Call Park Queue</td></tr>
    <tr><td>*61</td><td>To Voicemail - Unauthenticated</td></tr>
    <tr><td>*62</td><td>To Voicemail - Password Only</td></tr>
    <tr><td>*66&lt;10 or 11 Digit phone number&gt;</td><td>Route Call Off-Net. This feature will route a call out through a carrier, instead of staying on Network.</td></tr>
    <tr><td>*67&lt;10 or 11 Digit phone number&gt;</td><td>To Connection w/ Privacy DID 11 Digit</td></tr>
    <tr><td>*67{ext}</td><td>To User w/ Privacy</td></tr>
    <tr><td>*69</td><td>Call Return</td></tr>
    <tr><td>*72&lt;10 or 11 Digit phone number or Extension number&gt;</td><td>Set Forward Destination (This feature will only forward to Device or External Number, forwarding to a user such as an Auto-Attendant must be done in the portal)</td></tr>
    <tr><td>*73</td><td>DeActivate Forward</td></tr>
    <tr><td>*74</td><td>Activate Night Mode (Requires Setup)</td></tr>
    <tr><td>*75</td><td>DeActivate Night Mode</td></tr>
    <tr><td>*78</td><td>Activate Do Not Disturb</td></tr>
    <tr><td>*79</td><td>DeActivate Do Not Disturb</td></tr>
    <tr><td>*80</td><td>Start Call Recording</td></tr>
    <tr><td>*81</td><td>Stop Call Recording</td></tr>
    <tr><td>*82</td><td>Pause Call Recording for 1 minute or until *83 (Unpause Call Recording), whichever comes first</td></tr>
    <tr><td>*83</td><td>Resume Call Recording from a paused state as a result of *82</td></tr>
    <tr><td>*88</td><td>Make Agent Available for all Queues the Agent is a member of (Online)</td></tr>
    <tr><td>*89</td><td>Make Agent Unavailable for all Queues the Agent is a member of (Offline)</td></tr>
    <tr><td>*90</td><td>Activate Forward Busy (This feature will only forward to Device or External Number, forwarding to a user such as an Auto-Attendant must be done in the portal)</td></tr>
    <tr><td>*91</td><td>DeActivate Forward Busy</td></tr>
    <tr><td>*92</td><td>Activate Forward No Answer (This feature will only forward to Device or External Number, forwarding to a user such as an Auto-Attendant must be done in the portal)</td></tr>
    <tr><td>*93</td><td>DeActivate Forward No Answer</td></tr>
    <tr><td>*97{ext}</td><td>Transfer to a 4-digit Extension</td></tr>
    <tr><td>*98{ext}</td><td>Transfer to a 3-digit Extension</td></tr>
    <tr><td>*99</td><td>Transfer to Self</td></tr>
    <tr><th>Shortcut</th><th>Feature Description</th></tr>
    <tr><td>7{ext}</td><td>Transfer a call directly to voicemail (3 or 4 digit extension)</td></tr>
    <tr><td>71[0-9]</td><td>Transfer a call to a Call Park Queue in the 710-719 Range for Parking without Callback</td></tr>
    <tr><td>72[0-9]</td><td>Transfer a call to a Call Park Queue in the 720-729 Range for Parking with Callback</td></tr>
    <tr><td>99{ext}</td><td>Auto Answer/Intercom (3 or 4 digit extension) <em>This feature does not work with SLA.</em></td></tr>
    <tr><td>099</td><td>Invoke the <span class="link">Account Code</span> feature</td></tr>
    <tr><td>5000</td><td>Unregistered Login to VMail (prompted for acct no and password)</td></tr>
    <tr><td>5001</td><td>Registered Login to VMail (prompted for password only)</td></tr>
    <tr><td>5002</td><td>Hot Desking Sign In</td></tr>
    <tr><td>5003</td><td>Request User's PIN then provides 2nd dialtone (useful for phones in public spaces)</td></tr>
  </table>

  <div class="page-foot"></div>
  <div class="page-number">6</div>

  <div class="wordmark wordmark--large"><span class="mark"></span>TELVANO</div>

  <div class="contact contact--email"><span class="rule"></span><span class="value">support@telvanocomms.com</span><span class="rule"></span></div>
  <div class="contact contact--phone"><span class="rule"></span><span class="value">(555) 014-2290</span><span class="rule"></span></div>
  <div class="contact contact--web"><span class="rule"></span><span class="value">www.telvanocomms.com</span><span class="rule"></span></div>
</body>
</html>
```